Business Card Design Project

for a second hand vintage clothing store. shop name is The Velvet Cupboard

Cards to be double sided

The name on the card is Joanna Whitfield

Information to put on card:

The Velvet Cupboard
Joanna Whitfield (no job title)
42/871 Dunmore St, Glenwick, Harbourview, NSW, 2041.
Mobile: 0412 905 261
Email: thevelvetcupboard@mailbox.com.au
Web: www.thevelvetcupboard.com.au

Target Market(s)

Women looking at vintage clothing

Industry/Entity Type

Clothing

```html
<!DOCTYPE html>
<html lang="en">
<head>
<meta charset="utf-8">
<title>The Velvet Cupboard – Business Cards</title>
<link href="https://fonts.googleapis.com/css2?family=Great+Vibes&family=Didact+Gothic&display=swap" rel="stylesheet">
<style>
  :root {
    --plum: #5a2036;
    --card-plum: #5b2137;
    --amber: #e08b26;
    --amber-line: #f0a447;
    --cream: #f4dba6;
    --name-orange: #e8902c;
    --detail-rust: #d0683a;
    --coral: #e0525a;
  }
  * { margin: 0; padding: 0; box-sizing: border-box; }
  html, body {
    width: 1200px;
    height: 801px;
    overflow: hidden;
    background: var(--plum);
  }
  .stage {
    position: relative;
    width: 1200px;
    height: 801px;
    background: var(--plum);
  }
  .backdrop {
    position: absolute;
    left: 21px; top: 21px;
    width: 1158px; height: 759px;
    background: var(--amber);
  }
  .backdrop-rule {
    position: absolute;
    inset: 9px;
    border: 1px solid var(--amber-line);
  }
  .card {
    position: absolute;
    background: var(--card-plum);
    border-radius: 44px 0 44px 0;
    box-shadow: 4px 8px 10px rgba(70, 30, 10, 0.45);
    overflow: hidden;
  }
  .card-front {
    left: 168px; top: 83px;
    width: 542px; height: 293px;
  }
  .brand-name {
    position: absolute;
    left: 0; right: 0; top: 124px;
    text-align: center;
    font-family: "Great Vibes", cursive;
    font-size: 48px;
    line-height: 1;
    color: var(--cream);
    white-space: nowrap;
  }
  .card-back {
    left: 462px; top: 399px;
    width: 544px; height: 296px;
  }
  .holder-name {
    position: absolute;
    left: 46px; top: 74px;
    font-family: "Great Vibes", cursive;
    font-weight: 400;
    font-size: 38px;
    line-height: 1;
    letter-spacing: 1px;
    color: var(--name-orange);
    white-space: nowrap;
  }
  .contact {
    position: absolute;
    left: 46px; top: 130px;
    font-family: "Didact Gothic", sans-serif;
    font-size: 15px;
    line-height: 20px;
    color: var(--detail-rust);
    list-style: none;
    white-space: nowrap;
  }
  .figure-art {
    position: absolute;
    left: 412px; top: 0;
    width: 110px; height: 296px;
    background: linear-gradient(180deg, rgba(224, 82, 90, 0) 0%, var(--coral) 12%, var(--coral) 50%, #3d1424 78%, #a8a83a 100%);
    opacity: 0.85;
  }
</style>
</head>
<body>
<main class="stage">
  <div class="backdrop"><div class="backdrop-rule"></div></div>

  <section class="card card-front" aria-label="Card front">
    <p class="brand-name">The Velvet Cupboard</p>
  </section>

  <section class="card card-back" aria-label="Card back">
    <h1 class="holder-name">Joanna Whitfield</h1>
    <ul class="contact">
      <li>42/871 Dunmore St, Glenwick,</li>
      <li>Harbourview, NSW, 2041</li>
      <li>Tel. No.: 0412 905 261</li>
      <li>Email: thevelvetcupboard@mailbox.com.au</li>
      <li>Web: www.thevelvetcupboard.com.au</li>
    </ul>
    <div class="figure-art" role="img" aria-label="Fashion illustration of a woman in a coral dress and yellow-green boots"></div>
  </section>
</main>
</body>
</html>
```